Solar Energy Technology Company - Solar Savings Analysis Flyer

I Have Included The Text Content I Want Put On An 8 1/2 " x 11" Flyer.

I Want To See It In One Page Format And In Tri-Fold Brochure Format.

It Needs To Grab And Captivate Prospective Customers, Awesome Graphics, Layout, Etc.

We Are A Cutting Edge Solar Energy Solutions & Technology Company.

We Need A World Class High Tech Look and Logo For Our Company Included On Our 8 1/2 x 11 Flyer & Trifold Brochure

Brightfold Venture Partners, LLC
"Forward Ideas Delivered"

Would Like A Black Gold And Electric Blue Color Scheme, However, We We Are Open To Seeing Your Creativity, Colors, Graphics Etc. For Consideration.

Target Market(s)

Homeowners Without Solar Panels On Their Roof

Industry/Entity Type

New Roof Top Solar Energy Producing Panel Technology Systems

Font styles to use
Serif

Requirements
Must have
• See My Attached Flyer/Trifold Brochure Display Content
Nice to have
• Gold Black And Electric Blue Color Scheme, Solar Theme Background Graphics

```html
<!DOCTYPE html>
<html lang="en">
<head>
<meta charset="utf-8">
<title>Sunward Home Energy – Solar Savings Flyer</title>
<link rel="stylesheet" href="https://fonts.googleapis.com/css2?family=Arimo:wght@400;700&family=Roboto+Condensed:wght@400;700&display=swap">
<style>
  :root {
    --page-bg: #e9e7e3;
    --paper: #ffffff;
    --orange: #f39c1a;
    --orange-deep: #ec7a2a;
    --charcoal: #2f3238;
    --navy: #273587;
    --ink: #1b1f24;
    --text-dark: #2a2a2a;
    --sky-top: #1b3fb8;
    --sky-mid: #5d93e0;
    --panel-blue: #1a4fc4;
    --panel-dark: #0f2a78;
  }
  * { box-sizing: border-box; margin: 0; padding: 0; }
  html, body {
    width: 1200px; height: 1200px; overflow: hidden;
    background: var(--page-bg);
  }
  .flyer {
    position: absolute; left: 167px; top: 40px;
    width: 866px; height: 1120px;
    background: var(--paper);
    box-shadow: 0 6px 24px rgba(0,0,0,.18);
    overflow: hidden;
    font-family: "Arimo", Arial, sans-serif;
  }
  .flyer__art { position: absolute; left: 0; top: 0; width: 866px; height: 670px; }
  .brand {
    position: absolute; left: 27px; top: 30px;
    display: flex; align-items: center; gap: 12px;
  }
  .brand__name {
    font-family: "Arimo", Arial, sans-serif; font-weight: 700;
    font-size: 34px; color: var(--ink); letter-spacing: -0.5px; line-height: 1;
  }
  .brand__mark { width: 26px; height: 26px; background: var(--orange); }

  .headline-box {
    position: absolute; left: 0; top: 670px; width: 812px; height: 197px;
    background: var(--charcoal); border-radius: 0 6px 6px 0;
    padding: 14px 0 0 40px; color: #fff;
  }
  .headline-box__title {
    font-family: "Roboto Condensed", "Arial Narrow", sans-serif; font-weight: 700;
    font-size: 64px; line-height: 1; color: var(--orange); letter-spacing: 0.3px;
  }
  .headline-box__question {
    margin-top: 14px; font-weight: 700; font-size: 26px; letter-spacing: 0.4px;
  }
  .headline-box__offer {
    margin-top: 4px; font-weight: 700; font-size: 26px; letter-spacing: 0.4px;
    display: flex; align-items: baseline; gap: 10px;
  }
  .headline-box__amount { font-size: 58px; color: var(--orange); letter-spacing: 1px; }

  .pitch { position: absolute; left: 0; top: 873px; width: 866px; text-align: center; }
  .pitch__lead { font-weight: 700; font-size: 25px; color: var(--text-dark); padding-right: 30px; }
  .pitch__promise {
    margin-top: 6px; font-family: "Roboto Condensed", "Arial Narrow", sans-serif;
    font-weight: 700; font-size: 37px; color: var(--navy); line-height: 1.05;
  }
  .pitch__range {
    margin-top: 4px; font-family: "Roboto Condensed", "Arial Narrow", sans-serif;
    font-weight: 700; font-size: 28px; color: var(--text-dark);
  }
  .divider {
    position: absolute; left: 151px; top: 996px; width: 565px; height: 2px;
    background: linear-gradient(90deg, transparent, #444 20%, #444 80%, transparent);
  }
  .contact {
    position: absolute; left: 0; top: 1000px; width: 866px; text-align: center;
    font-weight: 700; font-size: 22.5px; color: var(--ink); white-space: nowrap;
  }
  .contact__company { color: var(--navy); }
  .tagline-band {
    position: absolute; left: 0; top: 1031px; width: 866px; height: 46px;
    background: var(--navy); color: #fff; text-align: center;
    font-weight: 700; font-size: 26px; line-height: 46px; letter-spacing: 0.4px;
  }
  .office-band {
    position: absolute; left: 0; top: 1077px; width: 866px; height: 43px;
    background: linear-gradient(90deg, var(--orange), var(--orange-deep));
    display: flex; justify-content: center; align-items: center; gap: 22px;
    font-family: "Roboto Condensed", "Arial Narrow", sans-serif;
    font-size: 17px; color: var(--navy);
  }
</style>
</head>
<body>
  <main class="flyer">
    <svg class="flyer__art" viewBox="0 0 866 670" xmlns="http://www.w3.org/2000/svg">
      <defs>
        <linearGradient id="solarFieldTone" x1="0" y1="0" x2="0.3" y2="1">
          <stop offset="0" stop-color="var(--sky-top)"/>
          <stop offset="0.35" stop-color="var(--sky-mid)"/>
          <stop offset="0.6" stop-color="var(--panel-blue)"/>
          <stop offset="1" stop-color="var(--panel-dark)"/>
        </linearGradient>
      </defs>
      <polygon class="accent accent--top" fill="var(--orange)" points="743,0 866,0 866,170 665,306 665,108"/>
      <polygon class="accent accent--left" fill="var(--orange)" points="0,339 155,263 155,670 0,670"/>
      <polygon class="accent accent--bottom" fill="var(--orange)" points="685,571 731,571 592,670 518,670"/>
      <polygon class="hero-photo" role="img" aria-label="Photo of tilted solar panel arrays in a field under a blue sky with white clouds"
        fill="url(#solarFieldTone)" points="530,55 806,55 812,61 812,463 518,670 41,670 41,391 47,385"/>
    </svg>

    <div class="brand">
      <span class="brand__name">SUNWARD HOME ENERGY</span>
      <span class="brand__mark"></span>
    </div>

    <section class="headline-box">
      <h1 class="headline-box__title">ATTENTION HOMEOWNER!</h1>
      <p class="headline-box__question">Are You FED UP With Your HIGH Electric Bills?</p>
      <p class="headline-box__offer">We Will Pay You <span class="headline-box__amount">$2,000…</span></p>
    </section>

    <section class="pitch">
      <p class="pitch__lead">…When You Allow Us To</p>
      <p class="pitch__promise">PERMANENTLY LOWER YOUR ELECTRIC BILL</p>
      <p class="pitch__range">By At Least 25% To 50%!</p>
    </section>

    <div class="divider"></div>
    <p class="contact"><span class="contact__company">Brightfold Venture Partners, LLC</span> 888-555-0142 Ext. 210 Dana Mercer</p>
    <p class="tagline-band">“Forward Ideas Delivered”</p>
    <footer class="office-band">
      <span>Corp Office: 4120 W. Cedar Ave. Las Vegas, NV 89100</span>
      <span>|</span>
      <span>Regional Office: 1785 Orchard Ave. Clovis, CA 93600</span>
    </footer>
  </main>
</body>
</html>
```